Film Poster Design For Japanese Film Poster #2

The title of this colour film is KAZE YAMA TSUKI HOSHI春 夏 秋 冬Translated this is literallySpring Summer Fall Winter ... however the English title is FOUR SEASONSWe attached a series of screen shots from the film and also the computer generated Kanji characters. We will be updating the brief with the Japanese title characters which currently being hand painted.We require the post in two formats. One being the traditional poster format and the other being in a wide screen ration of 1000px by 465px. Same design.This is a drama, feature length film comprising of four separate stories. The is mixture of Japanese and English dialogue. We are looking at 2 possible designs. You can choose to submit either.1: A with lots of white space ... focussing on smaller images at the Japanese text. I have uploaded a sample poster as a very rough indication. "Stories nobody ever wrote down about the quiet ones" / "Odile Bettina Rue Ingrid" - Lots of white space.Ideally we would have liked to have had the image of the young girl in the kimono pulling on the bell rope clear cut and used on white as a single main image. However, we are not sure that the clarity or resolution of the original image is sufficient. 2: One with lots of images as you can see with the two "Bridge Of Dust" Sample posters.Obviously we are not looking for a copy of either poster, but these posters are a guide to the two looks we are after.Thanks. Kaede
Hello all,Apologies for the delay. We have had to work through some naming issues.The film's English title has had to be renamed to THE LANTERNS. Please do not used TEN LANTERNS in any designed moving forward.Thanks Kaede Added Sunday, May 25, 2014

```html
<!DOCTYPE html>
<html lang="en">
<head>
<meta charset="utf-8">
<title>THE LANTERNS — Wind Mountain Moon Star</title>
<link rel="stylesheet" href="https://fonts.googleapis.com/css2?family=Arimo&family=Yuji+Boku&display=swap">
<style>
  :root {
    --paper: #ffffff;
    --caption: #808080;
    --wind-a: #8a2f1c;
    --wind-b: #5f6b2a;
    --wind-c: #2f3a1a;
    --mountain-a: #c9a06a;
    --mountain-b: #7a4a22;
    --mountain-c: #2a1a10;
    --moon-a: #e08a2a;
    --moon-b: #b5461a;
    --moon-c: #3a1e10;
    --star-a: #dfe8f2;
    --star-b: #1e2226;
    --star-c: #3d74b8;
  }
  html, body {
    margin: 0;
    padding: 0;
    overflow: hidden;
    background: var(--paper);
  }
  .poster {
    position: relative;
    width: 1200px;
    height: 558px;
    background: var(--paper);
    overflow: hidden;
  }
  .title {
    margin: 0;
  }
  .title-kanji {
    position: absolute;
    top: 51px;
    font-family: "Yuji Boku", serif;
    font-weight: 400;
    font-size: 235px;
    line-height: 1;
    color: transparent;
    -webkit-background-clip: text;
    background-clip: text;
    transform: translateX(-50%);
  }
  .kanji-wind     { left: 236px; background-image: linear-gradient(160deg, var(--wind-a) 10%, var(--wind-b) 55%, var(--wind-c) 100%); }
  .kanji-mountain { left: 448px; background-image: linear-gradient(170deg, var(--mountain-a) 0%, var(--mountain-b) 55%, var(--mountain-c) 100%); }
  .kanji-moon     { left: 672px; background-image: linear-gradient(150deg, var(--moon-a) 0%, var(--moon-b) 50%, var(--moon-c) 100%); }
  .kanji-star     { left: 946px; background-image: linear-gradient(180deg, var(--star-a) 0%, var(--star-b) 45%, var(--star-b) 80%, var(--star-c) 100%); }

  .caption {
    position: absolute;
    top: 336px;
    margin: 0;
    font-family: "Arimo", Arial, sans-serif;
    font-size: 26px;
    line-height: 35px;
    color: var(--caption);
    text-transform: uppercase;
    letter-spacing: -0.3px;
    white-space: nowrap;
  }
  .caption-translation { left: 144px; }
  .caption-english-title { left: 838px; }
  .caption span { display: block; }
</style>
</head>
<body>
  <main class="poster">
    <h1 class="title" role="img" aria-label="Brush-painted title characters 風 山 月 星, each filled with film scenery">
      <span class="title-kanji kanji-wind" aria-hidden="true">風</span>
      <span class="title-kanji kanji-mountain" aria-hidden="true">山</span>
      <span class="title-kanji kanji-moon" aria-hidden="true">月</span>
      <span class="title-kanji kanji-star" aria-hidden="true">星</span>
    </h1>
    <p class="caption caption-translation">
      <span>Wind</span>
      <span>Mountain</span>
      <span>Moon</span>
      <span>Star</span>
    </p>
    <p class="caption caption-english-title">THE LANTERNS</p>
  </main>
</body>
</html>
```